Fernvale Pte Ltd

I want a creative and stand out web page so when my client search for my web page or google search. The front page is stand out and they know that we are the interior office designer that are searching for . We are commercial office design company. We also have the video to put at our front page for client to see. Natural is the key elements. As we like to carry recycle materials , plant , trees is our key element such as biophilic design
Updates

Hi All,

For my web page, I need minimalist design and creative frontpage.
When my client search for my web page, they straight feel that this is the office design company.
The webpage is special and nature is the key element for the design.
My company logo can be design in the shaped of the letter OO in the webpage.
Below is the sample you can refer.

https://www.pinboardly.example/pin/592716408361528037/

Target Market(s)

Customer searching for office design

Industry/Entity Type

Commerical designer firm- Office interior design & Build company

Number of Pages Required

5+ page

Font styles to use
Other font styles liked:
• Wilmina

Colors
59FF00
82FF00
B8FF75
E3FFCB
F4FFEA
FFC000
F8CF3A
FAE287
FDF2CF
FEFAEE
6B429C
8869AF
B7A5CE
E3DAEB
F3F0F8

Requirements
Must have
• Home, Services,Gallery, Calculator, Testimonials, Contact, Blog
Nice to have
• Natural, creative, minimalist
Should not have
• No black color or blue color

```html
<!DOCTYPE html>
<html lang="en">
<head>
<meta charset="utf-8">
<title>Fernvale Pte Ltd — Office Interior Design</title>
<link rel="stylesheet" href="https://fonts.googleapis.com/css2?family=Questrial&family=Montserrat:wght@400;500;600&display=swap">
<style>
:root{
  --brand:#6a8a12;
  --brand-solid:#7e9a2a;
  --ink:#333;
  --muted:#8a8a8a;
  --nav:#666;
  --band:#f3f3f3;
  --field:#efefef;
  --white:#fff;
  --chat-btn:#21302a;
}
*{margin:0;padding:0;box-sizing:border-box}
html,body{width:743px;height:1200px;overflow:hidden;background:var(--white)}
body{position:relative;font-family:"Montserrat",sans-serif;color:var(--ink)}
.abs{position:absolute}

.site-name{font-family:"Questrial",sans-serif;color:var(--brand);letter-spacing:1.5px;font-size:17px;line-height:20px}
.site-logo{left:48px;top:20px}

.main-nav{right:36px;top:42px;font-size:7px;letter-spacing:.5px;color:var(--nav);display:flex;gap:5px}
.main-nav .sep{color:#999}

.hero{left:48px;top:72px;width:695px;height:292px;background:linear-gradient(160deg,#e9e6e0 0%,#c9b69d 40%,#b4875a 62%,#a79c8c 100%)}
.hero-btn{top:199px;width:38px;height:38px;background:var(--white);display:flex;align-items:center;justify-content:center;font-size:8px;color:#555}
.hero-pager{left:598px;top:320px;width:145px;height:44px;background:var(--white);display:flex;align-items:center;gap:14px;padding-left:34px;font-size:6px;font-weight:600;color:#111}
.hero-pager .line{width:16px;height:1px;background:#bbb;margin-left:-8px}
.hero-pager .off{color:#999}

.intro-title{left:47px;top:378px;width:345px;font-family:"Questrial",sans-serif;font-weight:400;font-size:19.8px;line-height:26.4px;color:var(--brand)}
.intro-copy{left:47px;width:340px;font-size:5.1px;line-height:9.9px;color:var(--muted);text-transform:uppercase}
.intro-photo{left:458px;top:385px;width:230px;height:345px;background:linear-gradient(180deg,#eeeeee 0%,#dcdad0 35%,#c9b547 52%,#8a6a3c 75%,#3b2e26 100%)}

.section-title{left:47px;top:752px;font-family:"Questrial",sans-serif;font-weight:400;font-size:19.8px;color:var(--brand);letter-spacing:.3px}
.project{top:787px;width:197px}
.project .thumb{height:131px}
.project h3{font-family:"Questrial",sans-serif;font-weight:400;font-size:13px;color:#333;margin-top:9px}
.project p{font-size:5.8px;color:#444;margin-top:2px}

.footer-band{left:47px;top:992px;width:696px;height:208px;background:var(--band)}
.footer-panel{left:90px;top:1034px;width:653px;height:166px;background:var(--white)}
.footer-logo{left:117px;top:1055px;font-size:16px}
.footer-head{top:1061px;width:95px;font-size:10px;letter-spacing:.8px;color:var(--brand);padding-bottom:4px;border-bottom:1px solid #e4e4e4}
.contact-list{left:235px;top:1088px;font-size:5.6px;line-height:11px;color:#555;text-transform:uppercase}
.newsletter{left:373px;top:1086px;display:flex}
.newsletter .field{width:134px;height:38px;background:var(--field);font-size:6px;color:#999;padding:15px 0 0 16px}
.newsletter .submit{width:57px;height:38px;background:var(--brand-solid);color:var(--white);font-size:5.5px;font-weight:600;display:flex;align-items:center;justify-content:center}
.footer-rule{left:236px;top:1159px;width:337px;height:1px;background:#e2e2e2}
.copyright{left:242px;top:1171px;font-size:5.6px;color:#555;letter-spacing:.3px}

.chat-bubble{left:569px;top:1136px;width:123px;height:48px;background:#f7f7f7;border-radius:4px;box-shadow:0 1px 3px rgba(0,0,0,.12);font-size:6.8px;line-height:12px;color:#222;padding:12px 8px}
.chat-close{position:absolute;right:6px;top:3px;font-size:7px;color:#ccc}
.chat-btn{left:681px;top:1174px;width:22px;height:22px;border-radius:50%;background:var(--chat-btn);display:flex;align-items:center;justify-content:center}
</style>
</head>
<body>

<div class="abs site-logo site-name">Fernvale</div>
<nav class="abs main-nav">
  <span>HOME</span><span class="sep">|</span><span>SERVICES</span><span class="sep">|</span><span>GALLERY</span><span class="sep">|</span><span>CALCULATOR</span><span class="sep">|</span><span>TESTIMONIALS</span><span class="sep">|</span><span>CONTACT</span><span class="sep">|</span><span>BLOG</span>
</nav>

<div class="abs hero" role="img" aria-label="Open-plan office lounge with green and orange chairs on a woven rug"></div>
<div class="abs hero-btn" style="left:60px">&#8249;</div>
<div class="abs hero-btn" style="left:694px">&#8250;</div>
<div class="abs hero-pager"><span>1</span><span>2</span><span class="off">3</span><span class="line"></span><span>4</span></div>

<h1 class="abs intro-title">Bring goods straight from factory and cut away the middleman costing so client can have a better quality with affordable price.</h1>
<p class="abs intro-copy" style="top:492px">Lorem ipsum dolor sit amet, consectetur adipiscing elit. Cras lacinia magna vel molestie faucibus. Donec auctor et urnalorem ipsum dolor sit amet, consectetur adipiscing elit. Cras lacinia magna vel molestie faucibus. Cras lacinia magna vel molestie faucibus. Donec auctor et urnalorem ipsum dolor sit amet, consectetur adipiscing elit. Cras lacinia magna vel molestie faucibus.</p>
<p class="abs intro-copy" style="top:542px">Lorem ipsum dolor sit amet, consectetur adipiscing elit. Cras lacinia magna vel molestie faucibus. Donec auctor et urnalorem ipsum dolor sit amet, consectetur adipiscing elit. Cras lacinia magna vel molestie faucibus. Cras lacinia magna vel molestie faucibus. Donec auctor et urnalorem ipsum dolor sit amet, consectetur adipiscing elit. Cras lacinia magna vel molestie faucibus.</p>
<div class="abs intro-photo" role="img" aria-label="Meeting area with yellow wall, glass partitions and dark lounge seating"></div>

<h2 class="abs section-title">OUR PORTFOLIO</h2>
<div class="abs project" style="left:48px">
  <div class="thumb" role="img" aria-label="Office floor with timber columns and indoor plants" style="background:linear-gradient(135deg,#3f4a2c 0%,#8a6a45 40%,#d8d5cc 70%,#c89a5c 100%)"></div>
  <h3>Project Name</h3><p>LOREM IPSUM DOLOR SIT AMET.</p>
</div>
<div class="abs project" style="left:269px">
  <div class="thumb" role="img" aria-label="Bright executive office with desk, chairs and a potted plant" style="background:linear-gradient(180deg,#f1f0ed 0%,#dedbd4 50%,#9a9894 100%)"></div>
  <h3>Project Name</h3><p>LOREM IPSUM DOLOR SIT AMET.</p>
</div>
<div class="abs project" style="left:491px">
  <div class="thumb" role="img" aria-label="Glass-walled meeting room beside a green moss wall and timber bench" style="background:linear-gradient(90deg,#6f7e86 0%,#cfd4d2 40%,#eae6df 65%,#8c7a4a 100%)"></div>
  <h3>Project Name</h3><p>LOREM IPSUM DOLOR SIT AMET.</p>
</div>

<div class="abs footer-band"></div>
<div class="abs footer-panel"></div>
<div class="abs footer-logo site-name">Fernvale</div>
<div class="abs footer-head" style="left:233px">CONTACTS</div>
<div class="abs contact-list">
  <div>Mail :hello@fernvale.example</div>
  <div>Adress :12 Mossgrove Lane</div>
  <div>Phone :+65 6100 2345</div>
</div>
<div class="abs footer-head" style="left:374px">NEWSLETTER</div>
<div class="abs newsletter"><div class="field">email</div><div class="submit">SUBMIT</div></div>
<div class="abs footer-rule"></div>
<div class="abs copyright">© FERNVALE. ALL RIGHTS RESERVED.</div>

<div class="abs chat-bubble"><span class="chat-close">✕</span>Hello! Do you have any questions? I'm happy to help.</div>
<div class="abs chat-btn">
  <svg width="11" height="11" viewBox="0 0 12 12" aria-hidden="true"><path d="M2 2h8a1 1 0 0 1 1 1v5a1 1 0 0 1-1 1H5l-3 2V3a1 1 0 0 1 1-1z" fill="#fff"/></svg>
</div>

</body>
</html>
```